Cedar Ridge Clay Range wordpress theme

I want a Wordpress theme that is classy, unusual, colorful, etc. based on my attached logo files.

Font:
- Serpentine-Bold-Bold for "CEDAR RIDGE"
- BrowalliaUPC for "CLAY RANGE"

Colors (CMYK code):
- BLACK ....... 0; 0; 0; 100;
- ORANGE ... gradient from 0; 65; 97.5; 0 to 0; 39; 97.5; 0

```html
<!DOCTYPE html>
<html lang="en">
<head>
<meta charset="utf-8">
<title>Cedar Ridge Clay Range</title>
<link rel="stylesheet" href="https://fonts.googleapis.com/css2?family=Open+Sans:wght@400;600;700;800&family=Raleway:wght@400;600;700&display=swap">
<style>
:root{
  --black:#0b0b0b;
  --panel:#141414;
  --line:#333;
  --orange:#f05a22;
  --orange-2:#f7941d;
  --white:#fff;
  --muted:#8a8a8a;
  --soft:#c9c9c9;
}
*{box-sizing:border-box;margin:0;padding:0}
html,body{width:1200px;height:2358px;overflow:hidden}
body{position:relative;background:radial-gradient(ellipse at 50% 30%,#4a4744 0%,#2b2927 55%,#161514 100%);font-family:"Open Sans",Arial,sans-serif;color:var(--white)}
.abs{position:absolute}
.orange-fill{background:linear-gradient(90deg,var(--orange),var(--orange-2))}
.photo{position:absolute}
.site-header{left:100px;top:0;width:1000px;height:132px;background:var(--black)}
.brand{left:144px;top:22px;width:190px;color:var(--orange);font-weight:800;font-size:19px;line-height:24px;letter-spacing:.5px;display:flex;align-items:center;gap:10px}
.brand .mark{width:18px;height:18px;background:var(--orange);flex:none}
.breaking{left:354px;top:0;width:746px;height:40px;font-size:11px;line-height:40px;padding-left:14px;white-space:nowrap;overflow:hidden}
.breaking b{font-weight:800;margin-right:12px}
.contact{top:52px;font-size:15px;display:flex;align-items:center;gap:10px}
.contact .ico{width:24px;height:24px;border-radius:50%;border:1px solid #666;display:flex;align-items:center;justify-content:center}
.socials{display:flex;gap:8px}
.socials span{width:26px;height:26px;border:1px solid #555;border-radius:3px;display:block}
.main-nav{left:360px;top:98px;width:740px;display:flex;justify-content:space-between;font-size:11px;font-weight:700;padding-right:6px}
.main-nav a{color:var(--white);text-decoration:none;padding:8px 12px;border-top:2px solid transparent;white-space:nowrap}
.main-nav a.active{border-top-color:var(--orange);background:#1e1e1e}
.hero{left:100px;top:136px;width:1000px;height:336px;background:linear-gradient(100deg,#232321 0%,#5e574a 18%,#b59c84 34%,#8a7a66 44%,#3b3833 58%,#181818 74%,#0e0e0e 100%)}
.offer{left:850px;top:178px;width:250px;height:254px;background:rgba(20,20,20,.75);text-align:center;padding-top:22px}
.offer .t1{font-size:20px}
.offer .t2{font-size:30px;margin-top:14px}
.offer .t3{font-size:26px;font-weight:800;margin-top:18px}
.offer .btn{display:inline-block;margin-top:14px;padding:6px 18px;font-size:26px}
.thumbs{left:100px;top:476px;width:1000px;height:88px;background:var(--black);display:flex;align-items:center;padding:0 42px;gap:9px}
.thumbs .th{width:80px;height:66px;border:2px solid #111}
.thumbs .th:nth-child(1){background:linear-gradient(135deg,#b29a80,#3a342c)}
.thumbs .th:nth-child(2){background:linear-gradient(135deg,#6e7a86,#2a2e33)}
.thumbs .th:nth-child(3){background:linear-gradient(135deg,#8c8a7a,#33352c)}
.thumbs .th:nth-child(4){background:linear-gradient(135deg,#c9b48e,#6a5a3e)}
.thumbs .th:nth-child(5){background:linear-gradient(135deg,#9a8a6a,#2e2a22)}
.thumbs .th:nth-child(6){background:linear-gradient(135deg,#c8a27a,#5a3a26)}
.thumbs .th:nth-child(7){background:linear-gradient(135deg,#7a7f70,#2c2f28)}
.thumbs .th:nth-child(8){background:linear-gradient(135deg,#a89070,#3c3024)}
.thumbs .th:nth-child(9){background:linear-gradient(135deg,#b08a60,#4a3420)}
.thumbs .th:nth-child(10){background:linear-gradient(135deg,#8e8a84,#2e2c2a)}
.thumbs .th.on{border-color:var(--orange)}
.arrow{top:508px;width:20px;height:24px}
.section-title{font-family:"Raleway",sans-serif;font-weight:700;font-size:19px}
.card{top:686px;width:184px;height:236px;background:var(--panel)}
.card .img{height:176px}
.card h4{color:var(--orange);font-size:13px;font-weight:700;padding:8px 10px 0}
.card p{color:var(--muted);font-size:10px;padding:2px 10px}
.quote{left:720px;top:686px;width:380px;height:88px;padding:12px 16px;font-size:12px;font-weight:600;line-height:18px}
.quote:before{content:"";position:absolute;left:-10px;top:14px;border:10px solid transparent;border-right-color:var(--orange);border-left:0}
.booking{left:100px;top:964px;width:1000px;height:163px;background:#fff}
.booking .pic{left:0;top:0;width:310px;height:163px;background:linear-gradient(90deg,#2e2d2b 0%,#6b6761 40%,#b8b5b0 75%,#eeeeee 100%)}
.booking h3{left:340px;top:26px;font-family:"Raleway",sans-serif;font-size:32px;font-weight:700;color:#222}
.booking h3 em{font-style:normal;color:var(--orange)}
.booking p{left:340px;top:82px;width:360px;font-size:11px;color:#333;line-height:16px}
.booking .side{left:730px;top:0;width:270px;height:163px;background:#252525;padding:30px 26px}
.booking .side h4{font-size:22px;font-weight:400}
.booking .side .price{color:var(--muted);font-size:11px;margin-top:24px}
.booking .side .price b{font-size:20px;color:#bbb;font-weight:400}
.btn-or{display:inline-block;color:#fff;font-size:13px;font-weight:700;padding:6px 14px}
.news{left:100px;top:1160px;width:318px;height:517px;background:var(--panel)}
.news h3{position:absolute;left:16px;top:24px;font-size:19px;font-weight:700}
.news .socials{position:absolute;left:160px;top:22px}
.news .socials span{border-radius:50%;width:26px;height:26px}
.news-item{position:absolute;left:14px;width:294px;height:70px}
.news-item .av{position:absolute;left:0;top:4px;width:62px;height:62px;border-radius:50%}
.news-item h5{position:absolute;left:80px;top:4px;font-size:16px;font-weight:400;color:#555}
.news-item p{position:absolute;left:80px;top:30px;font-size:9px;color:var(--muted);line-height:13px;width:200px}
.timings{left:747px;top:1160px;width:353px;height:253px;background:var(--panel)}
.timings h3{position:absolute;left:18px;top:22px;font-size:19px;font-weight:700}
.time-row{position:absolute;left:18px;width:320px;font-size:13px;color:#555;font-weight:600;padding-bottom:10px;border-bottom:1px solid var(--line)}
.time-row b{color:var(--orange)}
.tile{top:1436px;height:241px;background:var(--panel)}
.tile h3{position:absolute;left:14px;top:14px;font-size:18px;font-weight:700}
.tile .img{position:absolute;left:14px;top:52px;right:14px;height:176px}
.ev-text{font-size:10px;color:var(--soft);line-height:15px}
.ev-text .date{color:#888;font-size:9px}
.ev-text h5{font-size:13px;font-weight:700;margin:8px 0 14px}
.ev-text a{color:var(--orange);font-size:13px;font-weight:700;text-decoration:none}
.footer{left:0;top:1983px;width:1200px;height:250px;background:#111}
.footer h3{font-size:19px;font-weight:700}
.bottom{left:0;top:2240px;width:1200px;height:118px;background:#0a0a0a}
.pay{width:38px;height:24px;background:#3a3a3a;border-radius:2px}
</style>
</head>
<body>

<header class="abs site-header"></header>
<div class="abs brand"><span class="mark"></span><span>CEDAR RIDGE<br>CLAY RANGE</span></div>
<div class="abs breaking orange-fill"><b>BREAKING NEWS:</b>Lorem Ipsum passages, and more recently with desktop publishing software. &nbsp;FRIDAY 8TH JUNE 2012, 04:56:48 PM</div>

<div class="abs contact" style="left:472px">
  <span class="ico"><svg width="12" height="10" viewBox="0 0 12 10"><rect x=".5" y=".5" width="11" height="9" fill="none" stroke="#fff"/><path d="M.5 .5 6 5l5.5-4.5" fill="none" stroke="#fff"/></svg></span>
  info@cedarridgeclay.com
</div>
<div class="abs contact" style="left:768px">
  <span class="ico"><svg width="12" height="12" viewBox="0 0 12 12"><path d="M2 1l2 0 1 3-1.5 1a7 7 0 0 0 3.5 3.5L8 7l3 1v2a1 1 0 0 1-1 1A9 9 0 0 1 1 2a1 1 0 0 1 1-1z" fill="#fff"/></svg></span>
  <b>+1-615-555-0187</b>
</div>
<div class="abs socials" style="left:966px;top:51px"><span></span><span></span><span></span><span></span></div>

<nav class="abs main-nav">
  <a class="active" href="#">HOME</a><a href="#">ABOUT US</a><a href="#">HUNTING</a><a href="#">SHOOTING</a><a href="#">MEMBERSHIP</a><a href="#">TRAINING</a><a href="#">SAFETY</a><a href="#">BLOG</a><a href="#">CONTACT US</a>
</nav>

<div class="abs hero" role="img" aria-label="Shooter in safety glasses aiming a revolver"></div>
<div class="abs offer">
  <div class="t1">ONLINE ONLY OFFER</div>
  <div class="t2">12 Months</div>
  <div class="t3">MEMBERSHIP</div>
  <div class="btn orange-fill">Only $299</div>
</div>

<div class="abs thumbs" role="img" aria-label="Slider thumbnails of range photos">
  <div class="th"></div><div class="th"></div><div class="th"></div><div class="th on"></div><div class="th"></div><div class="th"></div><div class="th"></div><div class="th"></div><div class="th"></div><div class="th"></div>
</div>
<svg class="abs arrow" style="left:108px" viewBox="0 0 20 24"><path d="M14 3 5 12l9 9" fill="none" stroke="#fff" stroke-width="4"/></svg>
<svg class="abs arrow" style="left:1072px" viewBox="0 0 20 24"><path d="M6 3l9 9-9 9" fill="none" stroke="#fff" stroke-width="4"/></svg>

<h2 class="abs section-title" style="left:100px;top:616px">Lorem Ipsum passages, and more recently.</h2>
<div class="abs card" style="left:100px"><div class="img" style="background:linear-gradient(160deg,#9aa0a6 0%,#5d6368 45%,#2c2f32 100%)" role="img" aria-label="Rack of rifles"></div><h4>Gun Selection</h4><p>the largest selection</p></div>
<div class="abs card" style="left:296px"><div class="img" style="background:linear-gradient(160deg,#b7ab90 0%,#6f6a55 45%,#2f3328 100%)" role="img" aria-label="Instructor briefing shooters"></div><h4>Free Safety Briefings</h4><p>no experience needed to start</p></div>
<div class="abs card" style="left:493px"><div class="img" style="background:linear-gradient(160deg,#c4b596 0%,#7d7a5a 45%,#3a4530 100%)" role="img" aria-label="Shooter with ear protection"></div><h4>Membership</h4><p>Lorem ipsum passages</p></div>

<h2 class="abs section-title" style="left:715px;top:616px">What our Fans Say About Club</h2>
<div class="abs quote orange-fill">Lorem ipsum dolor sit amet, consectetur adipisicing elit, sed do eiusmod tempor incididunt ut labore et dolore magna aliqua.</div>
<div class="abs" style="left:720px;top:798px;font-size:13px;font-weight:700">Meet <span style="color:var(--orange)">OWEN HARLOW</span><div style="font-size:9px;color:var(--muted);font-weight:400;margin-top:4px">Anchor Person</div></div>
<div class="photo" style="left:938px;top:780px;width:162px;height:142px;background:linear-gradient(150deg,#e2d8c8 0%,#c2a888 40%,#4a5a3e 100%)" role="img" aria-label="Member portrait with ear protection"></div>

<section class="abs booking">
  <div class="abs pic" role="img" aria-label="Shooter aiming a shotgun"></div>
  <h3 class="abs">Schedule a <em>booking date</em></h3>
  <p class="abs">Nartys omnumerno lasec voluptas grostarya. Loremtator aut odit aut. Vmaquantur milatyas golorotas et joluam plamus oseqi nesciunt. Nosamo nequemero ipsumetos metrossos.</p>
  <div class="abs side"><h4>Go to <b>Booking Form</b></h4><div class="price">New Price<br><b>$125</b>/MONTH <span class="btn-or orange-fill" style="margin-left:36px">Book</span></div></div>
</section>

<section class="abs news">
  <h3>Latest News</h3>
  <div class="socials"><span></span><span></span><span></span><span></span></div>
  <div class="news-item" style="top:82px"><div class="av" style="background:linear-gradient(135deg,#b59a7e,#3e362c)" role="img" aria-label="News photo"></div><h5>Lorem ipsum dolor</h5><p>Nartys omnumerno lasec voluptas grostarya. Loremtator aut odit.</p></div>
  <div class="news-item" style="top:170px"><div class="av" style="background:linear-gradient(135deg,#8e9a86,#2c3328)" role="img" aria-label="News photo"></div><h5>Lorem ipsum dolor</h5><p>Nartys omnumerno lasec voluptas grostarya. Loremtator aut odit.</p></div>
  <div class="news-item" style="top:258px"><div class="av" style="background:linear-gradient(135deg,#c9a57c,#5a3a26)" role="img" aria-label="News photo"></div><h5>Lorem ipsum dolor</h5><p>Nartys omnumerno lasec voluptas grostarya. Loremtator aut odit.</p></div>
  <div class="news-item" style="top:346px"><div class="av" style="background:linear-gradient(135deg,#a0a4a8,#34373a)" role="img" aria-label="News photo"></div><h5>Lorem ipsum dolor</h5><p>Nartys omnumerno lasec voluptas grostarya. Loremtator aut odit.</p></div>
  <div class="news-item" style="top:434px"><div class="av" style="background:linear-gradient(135deg,#b8a488,#463a2c)" role="img" aria-label="News photo"></div><h5>Lorem ipsum dolor</h5><p>Nartys omnumerno lasec voluptas grostarya. Loremtator aut odit.</p></div>
</section>

<div class="photo" style="left:440px;top:1160px;width:307px;height:253px;background:linear-gradient(180deg,#d6cbb4 0%,#a39580 35%,#6a5d4c 70%,#3a332b 100%)" role="img" aria-label="Indoor shooting lanes"></div>
<section class="abs timings">
  <h3>Club Timings</h3>
  <div class="time-row" style="top:76px"><b>00:30</b> Lorem ipsum dolor</div>
  <div class="time-row" style="top:118px"><b>02:30</b> Lorem ipsum dolor</div>
  <div class="time-row" style="top:160px"><b>02:30</b> Lorem ipsum dolor</div>
  <span class="abs btn-or orange-fill" style="right:0;top:210px">MORE</span>
</section>

<section class="abs tile" style="left:440px;width:280px"><h3>Training Courses</h3><div class="img" style="background:linear-gradient(135deg,#c9a56a 0%,#9c7a46 45%,#5a4a32 100%)" role="img" aria-label="Instructor guiding a shooter"></div></section>
<div class="abs" style="left:769px;top:1436px;width:3px;height:241px;background:var(--orange)"></div>
<section class="abs tile" style="left:820px;width:280px"><h3>Guns &amp; accessories</h3><div class="img" style="background:linear-gradient(135deg,#3e2e22 0%,#8c4a2a 45%,#c8703e 70%,#2a1a14 100%)" role="img" aria-label="Shooter with red ear protection"></div></section>

<h2 class="abs" style="left:100px;top:1728px;font-size:19px;font-weight:700">Upcoming Events</h2>
<svg class="abs" style="left:1040px;top:1733px" width="56" height="24" viewBox="0 0 56 24"><circle cx="12" cy="12" r="11" fill="none" stroke="#777"/><path d="M14 7l-5 5 5 5" fill="none" stroke="#fff" stroke-width="2"/><circle cx="44" cy="12" r="11" fill="none" stroke="#777"/><path d="M42 7l5 5-5 5" fill="none" stroke="#fff" stroke-width="2"/></svg>
<div class="abs" style="left:100px;top:1780px;width:480px;height:159px;background:var(--panel)"></div>
<div class="photo" style="left:100px;top:1780px;width:193px;height:159px;background:linear-gradient(180deg,#c09a72 0%,#7a5e42 50%,#141414 52%,#1c1c1c 100%)" role="img" aria-label="Registration now sign with shooter"></div>
<div class="abs ev-text" style="left:322px;top:1800px;width:240px"><div class="date">January 15, 2014</div><h5>Membership Applications</h5>Nartys omnumerno lasec voluptas grostarya. Loremtator aut odit.<br><a href="#">View More</a></div>
<div class="abs" style="left:615px;top:1780px;width:485px;height:159px;background:var(--panel)"></div>
<div class="photo" style="left:615px;top:1780px;width:200px;height:159px;background:linear-gradient(180deg,#ffffff 0%,#f2f2f2 40%,#3a3a3a 62%,#111 100%)" role="img" aria-label="Annual meeting poster"></div>
<div class="abs ev-text" style="left:838px;top:1800px;width:240px"><div class="date">January 28, 2014</div><h5>Annual Membership Meeting</h5>Nartys omnumerno lasec voluptas grostarya. Loremtator aut odit.<br><a href="#">View More</a></div>

<footer class="abs footer">
  <h3 class="abs" style="left:120px;top:14px">Latest Reviews</h3>
  <div class="abs" style="left:120px;top:44px;font-size:30px;font-weight:800;line-height:1">&ldquo;</div>
  <p class="abs" style="left:120px;top:80px;width:280px;font-size:10px;line-height:15px;color:var(--soft)">Lorem ipsum dolor sit amet, consectetur adipiscing elit. Cras id turpis ac nibh ultricies sollicitudin. Donec sit amet magna sed justo fermentum gravida. Donec at sem nibh, vel euismod mauris.</p>
  <div class="abs" style="left:372px;top:150px;font-size:30px;font-weight:800;line-height:1">&rdquo;</div>
  <span class="abs btn-or orange-fill" style="left:120px;top:168px">View More</span>

  <h3 class="abs" style="left:455px;top:14px">Location</h3>
  <div class="abs" style="left:455px;top:50px;font-size:11px;color:var(--soft)">
    <svg width="10" height="10" viewBox="0 0 10 10"><path d="M9 1 1 4.5 4.5 5.5 5.5 9z" fill="#fff"/></svg> 21 Mill Road, Dixon</div>
  <div class="photo" style="left:455px;top:78px;width:285px;height:156px;background:linear-gradient(135deg,#ecebe7,#d3d0ca)" role="img" aria-label="Street map of the range location"></div>
  <svg class="abs" style="left:582px;top:104px" width="30" height="42" viewBox="0 0 30 42"><path d="M15 1C7 1 1 7 1 15c0 10 14 26 14 26s14-16 14-26C29 7 23 1 15 1z" fill="var(--orange)"/><circle cx="15" cy="15" r="6" fill="#fff"/></svg>

  <h3 class="abs" style="left:830px;top:14px">Opening Time</h3>
  <div class="abs" style="left:830px;top:50px;width:270px;font-size:10px;line-height:19px;color:var(--soft)">
    <div style="color:var(--orange)">Lorem ipsum dolor sit amet.</div>
    Monday-Friday: ________ 8.00 to 19.00<br>Saturday: ______________ 8.00 to 18.00<br>Sunday: ________________ 9.00 to 16.00<br>Every 30 day of month lorem ipsum dolor sit amet, consectetur adipiscing elit.
  </div>
</footer>

<div class="abs bottom">
  <div class="abs" style="left:100px;top:20px;display:flex;gap:6px"><div class="pay"></div><div class="pay"></div><div class="pay"></div><div class="pay"></div><div class="pay"></div></div>
  <div class="abs" style="left:462px;top:22px;width:210px;height:24px;background:#1c1c1c;font-size:10px;color:#999;line-height:24px;padding-left:8px">Sign Up For Our Newsletter</div>
  <span class="abs btn-or orange-fill" style="left:678px;top:22px;font-size:11px;padding:4px 14px">Subscribe</span>
  <div class="abs socials" style="left:990px;top:20px"><span style="border-radius:50%"></span><span style="border-radius:50%"></span><span style="border-radius:50%"></span><span style="border-radius:50%"></span></div>
  <div class="abs" style="right:100px;top:76px;font-size:10px;color:var(--soft)">Copyright &copy; 2013 All rights reserved</div>
</div>

</body>
</html>
```